Powerpoint Template for a cool IT Recruiting and Consulting Company

We need to have a PowerPoint template designed for our company. We are a Technology Consulting and Recruiting company in Canada.

I'm not looking for an explosion of colours, stay elegant and sharp.

The message that it needs to portray a cool tech company utilizing the blue in our logo but also professionalism and an excitement feel about it that makes clients want to do business with us.

I have attached 2 screenshots of the logo options and also the PDF of them.

Looking forward to seeing the results.

Target Market(s)

We sell our services to Banks, Government and other Tech Companies

Industry/Entity Type

It Service

Font styles to use
Sans Serif

Colors
0592cd

Requirements
Must have
• Logo
Nice to have
Should not have
• Lots of colours

```html
<!DOCTYPE html>
<html lang="en">
<head>
<meta charset="utf-8">
<title>Veritek Presentation Template</title>
<link href="https://fonts.googleapis.com/css2?family=Open+Sans:wght@400;600;700&display=swap" rel="stylesheet">
<style>
:root{
  --backdrop:#959595;
  --blue:#3f6e9d;
  --blue-dark:#2d5884;
  --blue-soft:#7b9fc2;
  --blue-pale:#dfe8f1;
  --grey-card:#6f6f6f;
  --paper:#ffffff;
  --ink:#666a70;
  --rule:#d5dbe2;
  --photo-a:#9bb2c6;
  --photo-b:#5f7f9c;
  --photo-warm:#b9a48f;
}
*{box-sizing:border-box;margin:0;padding:0}
html,body{width:761px;height:1200px;overflow:hidden;background:var(--backdrop)}
body{font-family:"Open Sans",Arial,sans-serif;color:var(--ink)}
.deck{position:absolute;left:66px;top:43px;display:grid;grid-template-columns:repeat(3,203px);grid-auto-rows:114px;gap:11px 10px}
.slide{position:relative;background:var(--paper);overflow:hidden;font-size:4.5px;line-height:1.35}
.slide--blue{background:var(--blue)}
.tag{position:absolute;top:6px;left:8px;font-size:4.5px;font-weight:700;color:var(--blue);letter-spacing:.3px}
.tag::before{content:"";display:inline-block;width:6px;height:1px;background:var(--blue);vertical-align:middle;margin-right:3px}
.abs{position:absolute}
.photo{position:absolute;background:linear-gradient(135deg,var(--photo-a),var(--photo-b))}
.photo--warm{background:linear-gradient(135deg,var(--photo-warm),var(--photo-b))}
.copy{position:absolute;color:var(--ink);font-size:4px}
.copy b{display:block;color:var(--blue);font-size:5px;margin-bottom:1px}
.white{color:#fff}
.white b{color:#fff}
.chip{position:absolute;width:11px;height:11px;border-radius:50%;background:var(--blue)}
.box{position:absolute;background:var(--blue)}
.heading{position:absolute;color:#fff;font-weight:700;font-size:9px}
table{border-collapse:collapse;font-size:3.6px;width:100%}
td,th{border:.5px solid var(--rule);padding:1px 2px;height:7px;text-align:left}
th{background:var(--blue);color:#fff;font-weight:600}
</style>
</head>
<body>
<main class="deck">

  <!-- Row 1 -->
  <section class="slide slide--blue">
    <div class="abs" style="inset:0;background:linear-gradient(120deg,#4a7aa8,#2d5884)"></div>
    <div class="abs" style="left:22px;top:44px;width:11px;height:11px;background:#fff"></div>
    <div class="abs" style="left:38px;top:40px;color:#fff;font-weight:700;font-size:15px">Veritek</div>
    <div class="copy white" style="left:38px;top:60px">Technology Consulting &amp; Recruiting</div>
  </section>

  <section class="slide">
    <div class="box" style="left:0;top:0;width:84px;height:114px"></div>
    <div class="copy white" style="left:8px;top:18px;width:68px"><b>About Us</b>Add your text here to describe the company.</div>
    <div class="photo" role="img" aria-label="Team working at a desk" style="left:90px;top:10px;width:52px;height:45px"></div>
    <div class="photo photo--warm" role="img" aria-label="Colleagues in a meeting" style="left:146px;top:10px;width:50px;height:45px"></div>
    <div class="photo photo--warm" role="img" aria-label="Office discussion" style="left:90px;top:59px;width:52px;height:45px"></div>
    <div class="photo" role="img" aria-label="Laptop work" style="left:146px;top:59px;width:50px;height:45px"></div>
  </section>

  <section class="slide">
    <div class="photo" role="img" aria-label="Team member portrait" style="left:30px;top:16px;width:24px;height:24px;border-radius:50%"></div>
    <div class="photo" role="img" aria-label="Team member portrait" style="left:90px;top:16px;width:24px;height:24px;border-radius:50%"></div>
    <div class="photo" role="img" aria-label="Team member portrait" style="left:150px;top:16px;width:24px;height:24px;border-radius:50%"></div>
    <div class="copy" style="left:20px;top:46px;width:45px;text-align:center"><b>Name</b>Position title here</div>
    <div class="copy" style="left:80px;top:46px;width:45px;text-align:center"><b>Name</b>Position title here</div>
    <div class="copy" style="left:140px;top:46px;width:45px;text-align:center"><b>Name</b>Position title here</div>
  </section>

  <!-- Row 2 -->
  <section class="slide">
    <div class="tag">TEXT HERE</div>
    <div class="photo" role="img" aria-label="Group of people" style="left:10px;top:18px;width:58px;height:38px"></div>
    <div class="photo photo--warm" role="img" aria-label="Business people" style="left:72px;top:18px;width:58px;height:38px"></div>
    <div class="photo" role="img" aria-label="Handshake meeting" style="left:134px;top:18px;width:58px;height:38px"></div>
    <div class="copy" style="left:10px;top:62px;width:58px"><b>Title</b>Short text goes here.</div>
    <div class="copy" style="left:72px;top:62px;width:58px"><b>Title</b>Short text goes here.</div>
    <div class="copy" style="left:134px;top:62px;width:58px"><b>Title</b>Short text goes here.</div>
  </section>

  <section class="slide">
    <div class="tag">TEXT HERE</div>
    <svg class="abs" style="left:0;top:0" width="203" height="114" viewBox="0 0 203 114" aria-hidden="true">
      <g fill="var(--blue)">
        <rect x="24" y="28" width="9" height="7" rx="1"/><rect x="68" y="28" width="9" height="7" rx="1"/>
        <rect x="112" y="28" width="9" height="7" rx="1"/><rect x="156" y="28" width="9" height="7" rx="1"/>
        <rect x="24" y="66" width="9" height="7" rx="1"/><rect x="68" y="66" width="9" height="7" rx="1"/>
        <rect x="112" y="66" width="9" height="7" rx="1"/><rect x="156" y="66" width="9" height="7" rx="1"/>
      </g>
    </svg>
    <div class="copy" style="left:14px;top:40px;width:30px;text-align:center">Add text</div>
    <div class="copy" style="left:58px;top:40px;width:30px;text-align:center">Add text</div>
    <div class="copy" style="left:102px;top:40px;width:30px;text-align:center">Add text</div>
    <div class="copy" style="left:146px;top:40px;width:30px;text-align:center">Add text</div>
    <div class="copy" style="left:14px;top:78px;width:30px;text-align:center">Add text</div>
    <div class="copy" style="left:58px;top:78px;width:30px;text-align:center">Add text</div>
    <div class="copy" style="left:102px;top:78px;width:30px;text-align:center">Add text</div>
    <div class="copy" style="left:146px;top:78px;width:30px;text-align:center">Add text</div>
  </section>

  <section class="slide">
    <div class="tag">TEXT HERE</div>
    <div class="photo" role="img" aria-label="Office building exterior" style="left:10px;top:18px;width:82px;height:86px"></div>
    <div class="box" style="left:110px;top:26px;width:12px;height:12px"></div>
    <div class="box" style="left:156px;top:26px;width:12px;height:12px"></div>
    <div class="box" style="left:110px;top:64px;width:12px;height:12px"></div>
    <div class="box" style="left:156px;top:64px;width:12px;height:12px"></div>
    <div class="copy" style="left:104px;top:42px;width:38px">Your text</div>
    <div class="copy" style="left:150px;top:42px;width:38px">Your text</div>
    <div class="copy" style="left:104px;top:80px;width:38px">Your text</div>
    <div class="copy" style="left:150px;top:80px;width:38px">Your text</div>
  </section>

  <!-- Row 3 -->
  <section class="slide">
    <div class="tag">TEXT HERE</div>
    <div class="copy" style="left:10px;top:24px;width:70px"><b>Growth</b>Add a short summary of the results here.</div>
    <svg class="abs" style="left:96px;top:26px" width="96" height="70" viewBox="0 0 96 70" aria-label="Bar chart">
      <g fill="var(--blue)">
        <rect x="4" y="44" width="9" height="22"/><rect x="18" y="34" width="9" height="32"/>
        <rect x="32" y="14" width="9" height="52"/><rect x="46" y="4" width="9" height="62"/>
        <rect x="60" y="24" width="9" height="42"/><rect x="74" y="38" width="9" height="28"/>
      </g>
      <line x1="0" y1="66.5" x2="96" y2="66.5" stroke="var(--rule)"/>
    </svg>
  </section>

  <section class="slide">
    <div class="abs" style="left:14px;top:14px;width:54px;height:86px;background:var(--blue)"></div>
    <div class="abs" style="left:74px;top:14px;width:54px;height:86px;background:var(--grey-card)"></div>
    <div class="abs" style="left:134px;top:14px;width:54px;height:86px;background:var(--blue)"></div>
    <div class="abs" style="left:35px;top:28px;width:12px;height:10px;background:#fff;border-radius:1px"></div>
    <div class="abs" style="left:95px;top:28px;width:12px;height:10px;background:#fff;border-radius:50%"></div>
    <div class="abs" style="left:155px;top:28px;width:12px;height:10px;background:#fff"></div>
    <div class="copy white" style="left:18px;top:48px;width:46px;text-align:center"><b>Title</b>Add text here</div>
    <div class="copy white" style="left:78px;top:48px;width:46px;text-align:center"><b>Title</b>Add text here</div>
    <div class="copy white" style="left:138px;top:48px;width:46px;text-align:center"><b>Title</b>Add text here</div>
  </section>

  <section class="slide slide--blue">
    <div class="abs" style="left:62px;top:52px;width:7px;height:7px;background:#fff"></div>
    <div class="heading" style="left:74px;top:48px">Section Title</div>
    <div class="copy white" style="left:74px;top:61px">Subtitle here</div>
  </section>

  <!-- Row 4 -->
  <section class="slide">
    <div class="tag">TEXT HERE</div>
    <div class="chip" style="left:48px;top:22px"></div>
    <div class="chip" style="left:48px;top:42px"></div>
    <div class="chip" style="left:48px;top:62px"></div>
    <div class="chip" style="left:48px;top:82px"></div>
    <div class="copy" style="left:66px;top:24px">Add your point here</div>
    <div class="copy" style="left:66px;top:44px">Add your point here</div>
    <div class="copy" style="left:66px;top:64px">Add your point here</div>
    <div class="copy" style="left:66px;top:84px">Add your point here</div>
  </section>

  <section class="slide slide--blue">
    <div class="abs" style="inset:0;background:linear-gradient(160deg,#4f80ae,#2d5884)"></div>
    <div class="photo" role="img" aria-label="Team at work" style="left:58px;top:26px;width:86px;height:50px;border:2px solid #fff"></div>
    <div class="copy white" style="left:58px;top:82px;width:86px;text-align:center">Add your caption</div>
  </section>

  <section class="slide">
    <div class="tag">TEXT HERE</div>
    <div class="abs" style="left:16px;top:20px;width:54px;height:38px;border:.5px solid var(--rule)"></div>
    <div class="abs" style="left:75px;top:20px;width:54px;height:38px;border:.5px solid var(--rule)"></div>
    <div class="abs" style="left:134px;top:20px;width:54px;height:38px;border:.5px solid var(--rule)"></div>
    <div class="abs" style="left:16px;top:64px;width:54px;height:38px;border:.5px solid var(--rule)"></div>
    <div class="abs" style="left:75px;top:64px;width:54px;height:38px;border:.5px solid var(--rule)"></div>
    <div class="abs" style="left:134px;top:64px;width:54px;height:38px;border:.5px solid var(--rule)"></div>
    <div class="chip" style="left:37px;top:25px"></div><div class="chip" style="left:96px;top:25px"></div><div class="chip" style="left:155px;top:25px"></div>
    <div class="chip" style="left:37px;top:69px"></div><div class="chip" style="left:96px;top:69px"></div><div class="chip" style="left:155px;top:69px"></div>
    <div class="copy" style="left:16px;top:42px;width:54px;text-align:center">Text here</div>
    <div class="copy" style="left:75px;top:42px;width:54px;text-align:center">Text here</div>
    <div class="copy" style="left:134px;top:42px;width:54px;text-align:center">Text here</div>
    <div class="copy" style="left:16px;top:86px;width:54px;text-align:center">Text here</div>
    <div class="copy" style="left:75px;top:86px;width:54px;text-align:center">Text here</div>
    <div class="copy" style="left:134px;top:86px;width:54px;text-align:center">Text here</div>
  </section>

  <!-- Row 5 -->
  <section class="slide">
    <div class="photo" role="img" aria-label="Glass office towers and trees" style="left:0;top:0;width:203px;height:114px;background:linear-gradient(120deg,#8fb0cf,#5f86a8 55%,#6d8f5e)"></div>
    <div class="abs" style="left:0;top:0;width:80px;height:114px;background:rgba(45,88,132,.85)"></div>
    <div class="copy white" style="left:10px;top:42px;width:62px"><b>Section Title</b>Add your text here</div>
  </section>

  <section class="slide">
    <div class="tag">TEXT HERE</div>
    <div class="box" style="left:0;top:22px;width:203px;height:58px"></div>
    <div class="abs" role="img" aria-label="Tablet screen" style="left:26px;top:36px;width:36px;height:28px;background:#e8eef4"></div>
    <div class="abs" role="img" aria-label="Desktop screen" style="left:76px;top:30px;width:52px;height:36px;background:#e8eef4"></div>
    <div class="abs" role="img" aria-label="Phone screen" style="left:144px;top:36px;width:18px;height:28px;background:#e8eef4"></div>
    <div class="chip" style="left:56px;top:88px;width:8px;height:8px"></div>
    <div class="chip" style="left:80px;top:88px;width:8px;height:8px"></div>
    <div class="chip" style="left:104px;top:88px;width:8px;height:8px"></div>
    <div class="chip" style="left:128px;top:88px;width:8px;height:8px"></div>
  </section>

  <section class="slide">
    <div class="tag">TEXT HERE</div>
    <div class="abs" style="left:10px;top:20px;width:183px">
      <table>
        <tr><th>Item</th><th>Plan A</th><th>Plan B</th><th>Plan C</th></tr>
        <tr><td>Text</td><td>00</td><td>00</td><td>00</td></tr>
        <tr><td>Text</td><td>00</td><td>00</td><td>00</td></tr>
        <tr><td>Text</td><td>00</td><td>00</td><td>00</td></tr>
        <tr><td>Text</td><td>00</td><td>00</td><td>00</td></tr>
        <tr><td>Text</td><td>00</td><td>00</td><td>00</td></tr>
        <tr><td>Text</td><td>00</td><td>00</td><td>00</td></tr>
        <tr><td>Text</td><td>00</td><td>00</td><td>00</td></tr>
      </table>
    </div>
  </section>

  <!-- Row 6 -->
  <section class="slide">
    <div class="tag">TEXT HERE</div>
    <div class="photo photo--warm" role="img" aria-label="Team silhouettes against a bright window" style="left:0;top:18px;width:203px;height:50px;background:linear-gradient(90deg,#6d8fb0,#c7b39a,#6d8fb0)"></div>
    <div class="copy" style="left:10px;top:76px;width:86px"><b>Our Team</b>Add a short text here.</div>
    <div class="copy" style="left:108px;top:76px;width:86px"><b>Our Goal</b>Add a short text here.</div>
  </section>

  <section class="slide">
    <div class="tag">TEXT HERE</div>
    <div class="abs" style="left:10px;top:20px;width:183px">
      <table>
        <tr><th>Name</th><th>Role</th><th>Year</th><th>Total</th></tr>
        <tr><td>Text</td><td>Text</td><td>00</td><td>00</td></tr>
        <tr style="background:var(--blue-pale)"><td>Text</td><td>Text</td><td>00</td><td>00</td></tr>
        <tr><td>Text</td><td>Text</td><td>00</td><td>00</td></tr>
        <tr style="background:var(--blue-pale)"><td>Text</td><td>Text</td><td>00</td><td>00</td></tr>
        <tr><td>Text</td><td>Text</td><td>00</td><td>00</td></tr>
      </table>
    </div>
  </section>

  <section class="slide">
    <div class="tag">TEXT HERE</div>
    <div class="copy" style="left:10px;top:28px;width:78px"><b>Services</b>Add a short description of the service here.</div>
    <div class="abs" role="img" aria-label="Desktop monitor showing a website" style="left:104px;top:22px;width:88px;height:56px;background:linear-gradient(135deg,#dfe8f1,#9fb9d2);border:2px solid #555"></div>
    <div class="abs" style="left:142px;top:80px;width:12px;height:8px;background:#999"></div>
  </section>

  <!-- Row 7 -->
  <section class="slide">
    <svg class="abs" style="left:0;top:0" width="203" height="114" viewBox="0 0 203 114" aria-label="Process diagram">
      <path d="M60 62 A42 42 0 0 1 143 62" fill="none" stroke="var(--blue)" stroke-width="12"/>
      <path d="M74 62 A28 28 0 0 1 129 62" fill="none" stroke="var(--grey-card)" stroke-width="8"/>
      <rect x="14" y="30" width="40" height="12" fill="var(--grey-card)"/>
      <rect x="149" y="30" width="40" height="12" fill="var(--grey-card)"/>
      <rect x="14" y="66" width="40" height="12" fill="var(--blue)"/>
      <rect x="149" y="66" width="40" height="12" fill="var(--blue)"/>
    </svg>
    <div class="copy white" style="left:14px;top:33px;width:40px;text-align:center">Step one</div>
    <div class="copy white" style="left:149px;top:33px;width:40px;text-align:center">Step two</div>
    <div class="copy white" style="left:14px;top:69px;width:40px;text-align:center">Step three</div>
    <div class="copy white" style="left:149px;top:69px;width:40px;text-align:center">Step four</div>
  </section>

  <section class="slide">
    <div class="photo" role="img" aria-label="Hands typing on a laptop" style="left:0;top:0;width:203px;height:114px;background:linear-gradient(120deg,#4d6f92,#9fb5c8)"></div>
    <div class="abs" style="left:10px;top:10px;width:70px;height:94px;background:rgba(45,88,132,.9)"></div>
    <div class="copy white" style="left:16px;top:40px;width:58px"><b>Section Title</b>Add your text here</div>
  </section>

  <section class="slide">
    <div class="tag">TEXT HERE</div>
    <svg class="abs" style="left:0;top:0" width="203" height="114" viewBox="0 0 203 114" aria-label="Organisation chart">
      <g stroke="var(--blue-soft)" stroke-width=".8" fill="none">
        <path d="M101 32 V42 M46 42 H156 M46 42 V50 M101 42 V50 M156 42 V50 M101 62 V70 M76 70 H126 M76 70 V78 M126 70 V78"/>
      </g>
      <g fill="var(--blue)">
        <rect x="82" y="20" width="38" height="12"/>
        <rect x="28" y="50" width="36" height="12"/><rect x="83" y="50" width="36" height="12"/><rect x="138" y="50" width="36" height="12"/>
        <rect x="58" y="78" width="36" height="12"/><rect x="108" y="78" width="36" height="12"/>
      </g>
    </svg>
  </section>

  <!-- Row 8 -->
  <section class="slide">
    <div class="tag">TEXT HERE</div>
    <div class="abs" style="left:14px;top:22px;width:80px;height:34px;background:var(--blue-pale);border-radius:3px"></div>
    <div class="abs" style="left:108px;top:58px;width:80px;height:34px;background:var(--blue);border-radius:3px"></div>
    <div class="copy" style="left:20px;top:28px;width:68px"><b>Question</b>Add your text here.</div>
    <div class="copy white" style="left:114px;top:64px;width:68px"><b>Answer</b>Add your text here.</div>
  </section>

  <section class="slide">
    <div class="tag">TEXT HERE</div>
    <div class="box" style="left:0;top:26px;width:203px;height:50px"></div>
    <div class="abs" role="img" aria-label="Laptop" style="left:70px;top:32px;width:62px;height:36px;background:#e8eef4;border:2px solid #444"></div>
    <div class="abs" style="left:62px;top:68px;width:78px;height:3px;background:#bbb"></div>
    <div class="copy" style="left:10px;top:84px;width:183px;text-align:center">Add a short caption here</div>
  </section>

  <section class="slide">
    <div class="tag">TEXT HERE</div>
    <div class="photo" role="img" aria-label="Meeting photo" style="left:12px;top:18px;width:56px;height:30px"></div>
    <div class="photo photo--warm" role="img" aria-label="Meeting photo" style="left:74px;top:18px;width:56px;height:30px"></div>
    <div class="photo" role="img" aria-label="Meeting photo" style="left:136px;top:18px;width:56px;height:30px"></div>
    <div class="photo photo--warm" role="img" aria-label="Meeting photo" style="left:12px;top:62px;width:56px;height:30px"></div>
    <div class="photo" role="img" aria-label="Meeting photo" style="left:74px;top:62px;width:56px;height:30px"></div>
    <div class="photo photo--warm" role="img" aria-label="Meeting photo" style="left:136px;top:62px;width:56px;height:30px"></div>
    <div class="copy" style="left:12px;top:50px">Caption</div><div class="copy" style="left:74px;top:50px">Caption</div><div class="copy" style="left:136px;top:50px">Caption</div>
    <div class="copy" style="left:12px;top:94px">Caption</div><div class="copy" style="left:74px;top:94px">Caption</div><div class="copy" style="left:136px;top:94px">Caption</div>
  </section>

  <!-- Row 9 -->
  <section class="slide">
    <div class="tag">TEXT HERE</div>
    <div class="abs" role="img" aria-label="World map with office locations" style="left:14px;top:18px;width:175px;height:60px;background:radial-gradient(ellipse at 50% 50%,#c9ced4,#e4e7ea 70%);border-radius:4px"></div>
    <div class="chip" style="left:50px;top:34px;width:6px;height:6px;background:#4aa39a"></div>
    <div class="chip" style="left:110px;top:40px;width:6px;height:6px;background:var(--blue)"></div>
    <div class="copy" style="left:14px;top:84px;width:84px"><b>Canada</b>Add text here</div>
    <div class="copy" style="left:106px;top:84px;width:84px"><b>Global</b>Add text here</div>
  </section>

  <section class="slide">
    <div class="tag">TEXT HERE</div>
    <div class="abs" role="img" aria-label="Abstract blue wave band" style="left:0;top:30px;width:203px;height:42px;background:linear-gradient(90deg,#cfdeed,#5f8bb6,#cfdeed)"></div>
    <div class="copy" style="left:14px;top:80px;width:50px;text-align:center">2015</div>
    <div class="copy" style="left:76px;top:80px;width:50px;text-align:center">2017</div>
    <div class="copy" style="left:138px;top:80px;width:50px;text-align:center">2019</div>
  </section>

  <section class="slide">
    <div class="photo photo--warm" role="img" aria-label="Colleagues collaborating around a table" style="left:0;top:0;width:203px;height:114px"></div>
    <div class="abs" style="left:10px;top:30px;width:78px;height:48px;background:rgba(45,88,132,.9)"></div>
    <div class="copy white" style="left:16px;top:40px;width:66px"><b>Thank You</b>Add contact text</div>
  </section>

</main>
</body>
</html>
```